Help keep hoosiers happy and at home!

We need a billboard designed for our Indiana based healthcare business called 'Willow Hearth Caregivers'. We administer a medicaid waiver program that provides support and financial aid to live in caregivers that take care of someone who would otherwise be in a nursing home or skilled nursing facility. Qualified caregivers could be eligible to receive up to 1200 dollars a month in tax free financial aid, as well as access to nursing support that helps manage any unexpected situations or changes in a care recipients condition or care routine. Our program empowers families to keep their loved ones at home and out of the nursing home. NOTE: We believe the tagline at the bottom of our logo is disproportionately small. We would like to see that tagline larger and easier to read. I look forward to seeing your design ideas!

Target Market(s)

Medicaid aged beneficiaries and caregivers.

Industry/Entity Type

Home Healthcare

Colors
0054AA
0677BA
7BADD7
CADEEF
E8F1F8

Requirements
Nice to have
• "Empowering friends and family to care for their loves ones at home. Eligible participants receive up to $15,000 a year, tax free."

```html
<!DOCTYPE html>
<html lang="en">
<head>
<meta charset="utf-8">
<title>Willow Hearth Caregivers – Billboard</title>
<link href="https://fonts.googleapis.com/css2?family=Montserrat:wght@400;600;700&display=swap" rel="stylesheet">
<style>
  :root {
    --navy: #283580;
    --navy-deep: #222e72;
    --blue-mid: #1f6fd0;
    --sky: #1e90e8;
    --photo-light: #7fbdf0;
    --panel-light: #eceef0;
    --panel-white: #ffffff;
    --text-grey: #5a5a5a;
    --stage: #d8d8d8;
  }
  html, body {
    margin: 0;
    padding: 0;
    width: 1016px;
    height: 1200px;
    overflow: hidden;
    background: var(--stage);
    font-family: "Montserrat", sans-serif;
  }
  .canvas {
    position: relative;
    width: 1016px;
    height: 1200px;
  }
  .billboard {
    position: absolute;
    left: 28px;
    top: 440px;
    width: 1461px;
    height: 487px;
    transform: scale(0.657);
    transform-origin: 0 0;
    background: var(--panel-white);
    box-shadow: 0 30px 40px rgba(0,0,0,0.35);
    overflow: hidden;
  }
  .billboard-shapes {
    position: absolute;
    inset: 0;
  }
  .brand-name {
    position: absolute;
    left: 0;
    top: 180px;
    width: 550px;
    text-align: center;
    color: var(--navy);
    font-weight: 700;
    font-size: 52px;
    line-height: 1.2;
    margin: 0;
  }
  .headline {
    position: absolute;
    left: 693px;
    top: 26px;
    margin: 0;
    color: #fff;
    font-size: 31px;
    line-height: 45.5px;
    font-weight: 700;
  }
  .headline .light { font-weight: 400; }
  .contact {
    position: absolute;
    left: 692px;
    top: 318px;
  }
  .contact-lead {
    margin: 0;
    color: var(--navy);
    font-weight: 600;
    font-size: 27px;
    line-height: 36px;
  }
  .contact-phone {
    margin: 0;
    color: var(--sky);
    font-weight: 700;
    font-size: 45px;
    line-height: 56px;
    letter-spacing: -0.5px;
  }
  .contact-web {
    margin: 0;
    color: var(--navy);
    font-weight: 700;
    font-size: 18.5px;
    line-height: 26px;
  }
  .contact-web .tld { font-weight: 400; color: var(--text-grey); }
  .divider {
    position: absolute;
    left: 1060px;
    top: 283px;
    width: 2px;
    height: 160px;
    background: var(--text-grey);
  }
  .offer {
    position: absolute;
    left: 1093px;
    top: 272px;
  }
  .offer-lead {
    margin: 0;
    color: var(--text-grey);
    font-size: 26px;
    line-height: 40px;
    font-weight: 400;
  }
  .offer-amount, .offer-note {
    margin: 0;
    font-weight: 700;
    font-size: 38px;
    line-height: 46px;
  }
  .offer-amount { color: var(--sky); }
  .offer-note { color: var(--navy); }
</style>
</head>
<body>
<main class="canvas">
  <section class="billboard" aria-label="Willow Hearth Caregivers billboard">
    <svg class="billboard-shapes" viewBox="0 0 1461 487" width="1461" height="487">
      <defs>
        <linearGradient id="bandGradient" x1="0" y1="0" x2="1" y2="0">
          <stop offset="0.35" stop-color="var(--navy)"/>
          <stop offset="0.8" stop-color="var(--blue-mid)"/>
          <stop offset="1" stop-color="var(--sky)"/>
        </linearGradient>
        <linearGradient id="photoGradient" x1="0" y1="0" x2="1" y2="0">
          <stop offset="0" stop-color="var(--blue-mid)" stop-opacity="0"/>
          <stop offset="0.35" stop-color="#3d8fe0"/>
          <stop offset="1" stop-color="var(--photo-light)"/>
        </linearGradient>
        <linearGradient id="panelGradient" x1="0" y1="0" x2="1" y2="0">
          <stop offset="0" stop-color="var(--panel-light)"/>
          <stop offset="1" stop-color="var(--panel-white)"/>
        </linearGradient>
      </defs>
      <rect x="611" y="243" width="850" height="244" fill="url(#panelGradient)"/>
      <polygon points="370,0 460,0 655,187 611,187 611,487 550,487 550,180" fill="var(--sky)"/>
      <polygon points="460,0 1461,0 1461,243 611,243 611,187 655,187" fill="url(#bandGradient)"/>
      <rect x="1130" y="0" width="331" height="243" fill="url(#photoGradient)" role="img" aria-label="Photo of a nurse helping an elderly woman with light arm exercises at home"/>
    </svg>

    <p class="brand-name">Willow Hearth<br>Caregivers</p>

    <h1 class="headline">Empowering<br>friends and family to care<br><span class="light">for their</span> loves ones<br>at home.</h1>

    <div class="contact">
      <p class="contact-lead">Call us today at</p>
      <p class="contact-phone">(800)555-0142</p>
      <p class="contact-web">willowhearthcaregivers<span class="tld">.com</span></p>
    </div>

    <div class="divider"></div>

    <div class="offer">
      <p class="offer-lead">Eligible participants<br>receive up to</p>
      <p class="offer-amount">$15,000 a year,</p>
      <p class="offer-note">tax free.</p>
    </div>
  </section>
</main>
</body>
</html>
```